British Columbia Day banner showcasing 20% off site

Banner graphic promoting our BC Day sale
Size: 1800 x 1000
- flag has been uploaded for inspiration
- examples from other companies and their sale banners have been uploaded for inspiration.
- product images can be found at www.mygreenleafhub.com, please use a variety of different products in this banner

Target Market(s)

19+

Industry/Entity Type

Cannabis

Requirements
Must have
• Phrases:
- “Celebrate BC Day with BC bud and companies”
- “20% off site wide sale*"
- Underneath phrase the date of sale “July 30th - August 3rd”
- In tiny print “*excludes all sale and bundled items”
- MUST BE 1800 X1000
Nice to have
• - images of the products or bud we carry which can be found at www.mygreenleafhub.com
- bold
Should not have
• - company logo

```html
<!DOCTYPE html>
<html lang="en">
<head>
<meta charset="utf-8">
<title>BC Day Site Wide Sale</title>
<link rel="stylesheet" href="https://fonts.googleapis.com/css2?family=Montserrat:wght@800&family=Source+Sans+3:wght@300;600;700&display=swap">
<style>
  :root {
    --sky-deep: #3a6dc2;
    --sky-mid: #4479cc;
    --cloud: rgba(255,255,255,0.22);
    --white: #ffffff;
    --gold: #fdb913;
    --flag-navy: #2b3f7a;
    --flag-red: #c8283a;
    --flag-gold: #d9a536;
    --bud-green: #7c8a5a;
    --bud-brown: #6b5a44;
    --pack-orange: #f08a2a;
    --pack-green: #5bb43c;
    --pack-pink: #e8426f;
  }
  * { margin: 0; padding: 0; box-sizing: border-box; }
  html, body { width: 1200px; height: 667px; overflow: hidden; }
  .banner {
    position: relative;
    width: 1200px;
    height: 667px;
    overflow: hidden;
    background:
      radial-gradient(ellipse 260px 90px at 110px 40px, var(--cloud), transparent 70%),
      radial-gradient(ellipse 300px 120px at 1140px 220px, var(--cloud), transparent 70%),
      radial-gradient(ellipse 280px 100px at 900px 420px, rgba(255,255,255,0.16), transparent 70%),
      linear-gradient(180deg, var(--sky-mid) 0%, var(--sky-deep) 55%, var(--sky-mid) 100%);
    font-family: "Source Sans 3", sans-serif;
    color: var(--white);
  }
  .headline {
    position: absolute;
    top: 50px;
    left: 0;
    width: 1200px;
    text-align: center;
    font-weight: 600;
    font-size: 50px;
    letter-spacing: 0.2px;
    line-height: 1;
  }
  .offer-frame {
    position: absolute;
    left: 82px;
    top: 131px;
    width: 1036px;
    height: 109px;
    border: 2px dashed var(--white);
    display: flex;
    align-items: center;
    justify-content: center;
  }
  .offer {
    font-family: "Montserrat", sans-serif;
    font-weight: 800;
    font-size: 75px;
    line-height: 1;
    letter-spacing: -1.5px;
    white-space: nowrap;
  }
  .offer-amount { color: var(--gold); }
  .sale-dates {
    position: absolute;
    right: 113px;
    top: 264px;
    font-weight: 700;
    font-size: 50px;
    line-height: 1;
  }
  .flag-photo {
    position: absolute;
    left: 25px;
    top: 234px;
    width: 525px;
    height: 433px;
    background: linear-gradient(180deg, var(--flag-navy) 0%, var(--flag-red) 35%, #e9e9f0 55%, var(--flag-navy) 72%, var(--flag-gold) 100%);
    border-radius: 6px 40px 30px 6px;
    opacity: 0.9;
  }
  .product-photo {
    position: absolute;
    top: 347px;
    height: 233px;
    border-radius: 8px;
  }
  .product-photo.buds {
    left: 553px;
    width: 170px;
    background: linear-gradient(135deg, var(--bud-green), var(--bud-brown));
  }
  .product-photo.packs {
    left: 724px;
    width: 440px;
    background: linear-gradient(90deg, #4a4e6e 0%, var(--pack-orange) 45%, var(--pack-green) 75%, var(--pack-pink) 100%);
  }
  .fine-print {
    position: absolute;
    right: 16px;
    bottom: 18px;
    font-weight: 300;
    font-size: 25px;
    line-height: 1;
  }
</style>
</head>
<body>
  <main class="banner">
    <h1 class="headline">Celebrate BC Day with BC bud and companies</h1>

    <div class="offer-frame">
      <p class="offer"><span class="offer-amount">20% OFF</span> SITE WIDE SALE</p>
    </div>

    <p class="sale-dates">July 30th - August 3rd</p>

    <div class="flag-photo" role="img" aria-label="Photo of the British Columbia flag waving on a flagpole against the sky"></div>

    <div class="product-photo buds" role="img" aria-label="Photo of two cannabis buds"></div>
    <div class="product-photo packs" role="img" aria-label="Photo of concentrate packages and fruit-flavoured gummy packs with gummies"></div>

    <p class="fine-print">*excludes all sale and bundled items</p>
  </main>
</body>
</html>
```